Nonna's Granary - Flour Bag Packing for Fit and Healthy Flour

Nonna's Granary is a family owned company that was incorporated in honor of our grandfather who is in the pic below. We would like to incorporate that picture into the packaging design. We would also like for the logo to represent a modern/fit lifestyle that is unique from the current competition.

Nonna's flour is a newly practiced style of milling that allows for flour to be consumed in its natural/organic state. We don't not bleach, chemically treat or add any enriched/preservative additives to our flour. This allows for freshness (our priority) and the natural flavors of the nutty grain to seep into our flour.

Our flour contains all the nutritional value that comes from all the components of Wheat Family Grains.

Our Family has been in the flour business for 60+ years and we established our mill in Debar Macedonia in 1998.

100% Organic
Non GMO
Family Owned
Stone Milled
Banner (Product Types): All Purpose Flour, Whole Wheat Flour, Pastry Flour, Artisan (Bread) Flour
Size: 1 KG / 5 KG / 25 KG

Flour is good for: Cookies, Cakes, Bread, Biscuits, Brownies, Muffins, Pastries, Pancakes, Rolls, Pizza Crust Pies

Target Market(s)

Fit Lifestyle, Hipsters, Modern, NYC

Industry/Entity Type

Agtech

Logo Text

Nonna's Granary

Requirements
Must have
• Nonna's Pic must be incorporated somehow on the bag. He will provide a friendly face and a homier feeling. The pic does not need to be the Center Piece. The logo will be the Center Piece.
Nice to have
• Nonna's Granary on the side of the bags or some cool/hip design.

```html
<!DOCTYPE html>
<html lang="en">
<head>
<meta charset="utf-8">
<title>Nonna's Flour – All Purpose Flour Bag</title>
<link href="https://fonts.googleapis.com/css2?family=Fredoka:wght@600&display=swap" rel="stylesheet">
<style>
  :root {
    --backdrop: #e4e4e4;
    --kraft: #b9a78b;
    --kraft-light: #c6b59a;
    --kraft-dark: #a8957a;
    --ink: #221f1c;
    --paper-white: #f6f1e8;
  }
  * { margin: 0; padding: 0; box-sizing: border-box; }
  html, body {
    width: 1200px;
    height: 1200px;
    overflow: hidden;
    background: var(--backdrop);
    font-family: "Fredoka", "Arial Rounded MT Bold", sans-serif;
  }
  .canvas {
    position: relative;
    width: 1200px;
    height: 1200px;
  }
  .bag-front {
    position: absolute;
    left: 290px;
    top: 90px;
    width: 620px;
    height: 1020px;
    background: linear-gradient(100deg, var(--kraft-dark) 0%, var(--kraft-light) 30%, var(--kraft) 70%, var(--kraft-dark) 100%);
  }
  .portrait-seal {
    position: absolute;
    left: 166px;
    top: 140px;
    width: 268px;
    height: 268px;
  }
  .brand-name {
    position: absolute;
    left: 0;
    width: 100%;
    top: 440px;
    text-align: center;
    color: var(--ink);
    font-weight: 600;
    font-size: 78px;
    line-height: 80px;
    letter-spacing: 1px;
  }
  .brand-name .line { display: block; }
  .brand-name .upper { text-transform: uppercase; }
  .product-banner {
    position: absolute;
    left: 90px;
    top: 640px;
    width: 440px;
    height: 68px;
  }
  .product-banner svg { position: absolute; inset: 0; }
  .product-banner .label {
    position: absolute;
    inset: 0;
    display: flex;
    align-items: center;
    justify-content: center;
    color: var(--paper-white);
    font-weight: 600;
    font-size: 34px;
  }
  .claims {
    position: absolute;
    left: 0;
    width: 100%;
    top: 758px;
    list-style: none;
    text-align: center;
    color: var(--paper-white);
    font-weight: 600;
    font-size: 25px;
    line-height: 32px;
  }
</style>
</head>
<body>
<main class="canvas">
  <section class="bag-front">
    <svg class="portrait-seal" viewBox="0 0 268 268" aria-hidden="false">
      <defs>
        <radialGradient id="portrait-tone" cx="50%" cy="45%" r="55%">
          <stop offset="0%" stop-color="#6f6458"/>
          <stop offset="70%" stop-color="#8f806b"/>
          <stop offset="100%" stop-color="#b9a78b"/>
        </radialGradient>
      </defs>
      <circle cx="134" cy="134" r="128" fill="none" stroke="var(--ink)" stroke-width="6"/>
      <circle cx="134" cy="134" r="112" fill="url(#portrait-tone)" role="img" aria-label="Portrait photo of the family grandfather"/>
    </svg>

    <h1 class="brand-name">
      <span class="line upper">Nonna’s</span>
      <span class="line">Flour</span>
    </h1>

    <div class="product-banner">
      <svg viewBox="0 0 440 68" preserveAspectRatio="none" aria-hidden="true">
        <polygon points="0,0 440,0 418,34 440,68 0,68 22,34" fill="var(--ink)"/>
      </svg>
      <span class="label">All Purpose Flour</span>
    </div>

    <ul class="claims">
      <li>100% Organic</li>
      <li>Non GMO</li>
      <li>Family Owned</li>
      <li>Stone Milled</li>
    </ul>
  </section>
</main>
</body>
</html>
```